Biz Cards to match new logo

I'm looking for a business card layout to go with my new logo. I'd like to have one side in colour (purple, with the logo in white) and the other side to be white with the purple logo and contact info in black font: name, address (2 lines), phone, email, fax, website. The logo includes the company name so it doesn't need to be repeated in the text. The font should be legibile to the semi-blind. (I hate small fonts on business cards).

Industry/Entity Type

Business

```html
<!DOCTYPE html>
<html lang="en">
<head>
<meta charset="utf-8">
<title>Meridian Research – Business Card</title>
<link rel="stylesheet" href="https://fonts.googleapis.com/css2?family=Open+Sans:wght@400&display=swap">
<style>
  :root {
    --brand-purple: #674188;
    --card-white: #ffffff;
    --ink: #3a3a3a;
    --stage: #e4e4e4;
  }
  * { box-sizing: border-box; margin: 0; padding: 0; }
  html, body {
    width: 1200px;
    height: 1200px;
    overflow: hidden;
  }
  body {
    background: var(--stage);
    font-family: "Open Sans", Arial, sans-serif;
    display: flex;
    align-items: center;
    justify-content: center;
    gap: 30px;
  }
  .card {
    width: 560px;
    height: 331px;
    position: relative;
    box-shadow: 0 4px 14px rgba(0,0,0,0.18);
    overflow: hidden;
  }

  /* Front: white side with contact details */
  .card--front { background: var(--card-white); }
  .card--front .wordmark {
    position: absolute;
    left: 0;
    width: 290px;
    top: 120px;
    text-align: center;
    color: var(--brand-purple);
    font-weight: 400;
    line-height: 1.25;
  }
  .wordmark__name {
    display: block;
    font-size: 34px;
    letter-spacing: 2px;
    text-transform: uppercase;
  }
  .wordmark__sub {
    display: block;
    font-size: 15px;
    letter-spacing: 6px;
    text-transform: uppercase;
  }
  .contact {
    position: absolute;
    left: 302px;
    top: 56px;
    color: var(--ink);
  }
  .contact__name {
    color: var(--brand-purple);
    font-size: 20px;
    line-height: 1.1;
    text-transform: uppercase;
  }
  .contact__title {
    color: var(--brand-purple);
    font-size: 14px;
    line-height: 1.2;
    text-transform: uppercase;
    margin-bottom: 10px;
  }
  .contact__address {
    font-size: 15px;
    line-height: 1.2;
    margin-bottom: 16px;
  }
  .contact__list { list-style: none; }
  .contact__item {
    display: flex;
    align-items: center;
    gap: 12px;
    font-size: 15px;
    line-height: 22px;
  }
  .contact__icon {
    width: 18px;
    height: 18px;
    flex: none;
  }
  .band {
    position: absolute;
    left: 0;
    right: 0;
    bottom: 0;
    height: 32px;
    background: var(--brand-purple);
  }

  /* Back: purple side with the name in white */
  .card--back {
    background: var(--brand-purple);
    display: flex;
    align-items: center;
    justify-content: center;
  }
  .card--back .wordmark {
    color: var(--card-white);
    text-align: center;
    font-weight: 400;
    line-height: 1.25;
    margin-top: 40px;
  }
  .card--back .wordmark__name { font-size: 40px; }
  .card--back .wordmark__sub { font-size: 17px; letter-spacing: 7px; }
</style>
</head>
<body>

  <section class="card card--front" aria-label="Business card, contact side">
    <div class="wordmark">
      <span class="wordmark__name">Meridian</span>
      <span class="wordmark__sub">Research</span>
    </div>

    <div class="contact">
      <p class="contact__name">Your Name</p>
      <p class="contact__title">Titel</p>
      <p class="contact__address">your address can put here<br>your address can put here</p>
      <ul class="contact__list">
        <li class="contact__item">
          <svg class="contact__icon" viewBox="0 0 18 18" aria-hidden="true">
            <rect width="18" height="18" rx="3" fill="#674188"/>
            <path d="M5.5 4.5 l2 0 l1 3 l-1.4 1 a6 6 0 0 0 2.4 2.4 l1-1.4 l3 1 l0 2 a1.5 1.5 0 0 1-1.5 1.5 a8 8 0 0 1-8-8 a1.5 1.5 0 0 1 1.5-1.5z" fill="#fff"/>
          </svg>
          012 456 789
        </li>
        <li class="contact__item">
          <svg class="contact__icon" viewBox="0 0 18 18" aria-hidden="true">
            <rect width="18" height="18" rx="3" fill="#674188"/>
            <rect x="4" y="7" width="10" height="6" rx="1" fill="#fff"/>
            <rect x="6" y="4" width="6" height="3" fill="#fff"/>
          </svg>
          012 456 789
        </li>
        <li class="contact__item">
          <svg class="contact__icon" viewBox="0 0 18 18" aria-hidden="true">
            <rect width="18" height="18" rx="3" fill="#674188"/>
            <rect x="4" y="5.5" width="10" height="7" fill="none" stroke="#fff" stroke-width="1.3"/>
            <path d="M4 5.5 l5 4 l5-4" fill="none" stroke="#fff" stroke-width="1.3"/>
          </svg>
          yourname@meridian.com
        </li>
        <li class="contact__item">
          <svg class="contact__icon" viewBox="0 0 18 18" aria-hidden="true">
            <rect width="18" height="18" rx="3" fill="#674188"/>
            <circle cx="9" cy="9" r="5" fill="none" stroke="#fff" stroke-width="1.2"/>
            <path d="M4 9 h10 M9 4 c-2.5 3-2.5 7 0 10 M9 4 c2.5 3 2.5 7 0 10" fill="none" stroke="#fff" stroke-width="1"/>
          </svg>
          www.meridian.com
        </li>
      </ul>
    </div>

    <div class="band"></div>
  </section>

  <section class="card card--back" aria-label="Business card, brand side">
    <div class="wordmark">
      <span class="wordmark__name">MERIDIAN</span>
      <span class="wordmark__sub">RESEARCH</span>
    </div>
  </section>

</body>
</html>
```